Design Cover for Catalog and theme pages to match cover design for continuity

I need a catalog cover for our new catalog and have it flow through the pages uniting the design together. Most the hardest work is complete however it needs a designers touch to bring it all together. The attached files include the catalog with products images data and logos. We have more assets however with the 100MB limit we are unable to upload to many more. For additional images you can pull them from our website www.brandowave.example.

Target Market(s)

Tradesmen and trades women who work in the Electrical and Industrial Automation spaces.

Industry/Entity Type

Industrial

Font styles to use
Sans Serif

Colors
3176b5
0555a3
85cae6

Requirements
Must have
• Complete cover design
• Must also have cover theme flow through remaining pages
Nice to have
• Header and Footer on each page
• Index on cover with page reference
Should not have
• This is not a redesign of the whole catalog, please don't drastically change the pages or any of the data in the tables.

```html
<!DOCTYPE html>
<html lang="en">
<head>
<meta charset="utf-8">
<title>Brandowave Catalogue Cover</title>
<link rel="stylesheet" href="https://fonts.googleapis.com/css2?family=Nunito+Sans:wght@400;600;900&display=swap">
<style>
  :root {
    --backdrop: #e6e6e6;
    --paper: #ffffff;
    --panel: #242325;
    --blue-light: #5aa5df;
    --blue-mid: #3176b5;
    --blue-deep: #2b3f8f;
    --navy: #2e3483;
    --text-light: #f2f2f2;
  }
  * { margin: 0; padding: 0; box-sizing: border-box; }
  html, body {
    width: 1200px; height: 1200px; overflow: hidden;
    background: var(--backdrop);
    font-family: "Nunito Sans", sans-serif;
  }
  .cover {
    position: absolute; left: 166px; top: 42px;
    width: 944px; height: 1213px;
    background: var(--paper);
    transform: scale(0.92); transform-origin: top left;
  }
  .cover-artwork {
    position: absolute; left: 0; top: 43px; width: 944px; height: 1127px;
    background: linear-gradient(160deg, #4a8fd0 0%, #3a74b8 40%, #2f5aa6 75%, #2c3f94 100%);
  }
  .column-rules { position: absolute; left: 0; top: 43px; }
  .brand-tab {
    position: absolute; left: 381px; top: 0; width: 190px; height: 188px;
    background: var(--panel);
  }
  .brand-name {
    position: absolute; left: 0; right: 0; top: 98px;
    text-align: center; color: var(--text-light);
    font-weight: 600; font-size: 31px; letter-spacing: 0.2px;
  }
  .brand-bar {
    position: absolute; left: 14px; top: 154px; width: 163px; height: 21px;
    background: linear-gradient(90deg, var(--blue-light), var(--navy));
  }
  .title-panel {
    position: absolute; left: 381px; top: 566px; width: 563px; height: 378px;
    background: var(--panel);
  }
  .title {
    position: absolute; left: 39px; top: 105px;
    color: #ffffff; font-weight: 900; font-size: 66px; line-height: 1;
  }
  .tagline {
    position: absolute; left: 39px; top: 185px;
    color: var(--blue-light); font-weight: 600; font-size: 24px;
  }
  .intro {
    position: absolute; left: 39px; top: 225px; width: 360px;
    color: var(--text-light); font-weight: 400; font-size: 17px; line-height: 22px;
  }
  .title-bar {
    position: absolute; left: 38px; top: 309px; right: 0; height: 35px;
    background: linear-gradient(90deg, var(--blue-light), var(--blue-mid) 45%, var(--navy));
  }
</style>
</head>
<body>
  <div class="cover">
    <div class="cover-artwork" role="img" aria-label="Close-up photograph of rows of blue industrial terminal block components"></div>
    <svg class="column-rules" width="944" height="1127" aria-hidden="true">
      <g stroke="#ffffff" stroke-opacity="0.75" stroke-width="1" stroke-dasharray="2 3">
        <line x1="94" y1="0" x2="94" y2="1127"/>
        <line x1="189.5" y1="0" x2="189.5" y2="1127"/>
        <line x1="285.5" y1="0" x2="285.5" y2="1127"/>
        <line x1="381" y1="0" x2="381" y2="1127"/>
        <line x1="477.5" y1="0" x2="477.5" y2="1127"/>
        <line x1="573" y1="0" x2="573" y2="1127"/>
        <line x1="668.5" y1="0" x2="668.5" y2="1127"/>
        <line x1="764.5" y1="0" x2="764.5" y2="1127"/>
        <line x1="860" y1="0" x2="860" y2="1127"/>
      </g>
    </svg>
    <div class="brand-tab">
      <div class="brand-name">Brandowave</div>
      <div class="brand-bar"></div>
    </div>
    <div class="title-panel">
      <h1 class="title">Catalogue</h1>
      <p class="tagline">Efficiency through simplicity.</p>
      <p class="intro">Our products and services are developed to maximize productivity with minimum waste of time and effort.</p>
      <div class="title-bar"></div>
    </div>
  </div>
</body>
</html>
```